Web design concept for a IT recruitment agency.

Our website addresses two different target groups:
- Customers (companies) wanting to hire new IT talent
- It talent to find a new JOB

We a looking for a visual design concept that either addresses both target groups in one of the following options:
a. target both groups in 1 single splash page.
b. target both groups in 2 different pages one for both groups
c. or any creative third concept you can come up with

Requirements, we want one overall visual concept, that both target groups can relate to.

Trigger words what we want to express:
- passion / drive
- knowhow
- involvement
- professional/yet playful
- engagement

Background, company culture:
We are a recruitment agency with over 15 years of experience, we have no hard-sale culture.
But we emphasize on long term relationships, showing real interest in people and their needs.

Design requirements:
Use logo
Flat contemporary design

Target Market(s)

Industry/Entity Type

Hire

Number of Pages Required

2 page

Requirements
Must have
• We a looking for a visual design concept that either addresses both target groups

```html
<!DOCTYPE html>
<html lang="en">
<head>
<meta charset="utf-8">
<title>Brightvale – IT Recruitment</title>
<link rel="stylesheet" href="https://fonts.googleapis.com/css2?family=Roboto+Condensed:wght@400;700&family=Montserrat:wght@400;500&family=Open+Sans:wght@400;600&display=swap">
<style>
  :root {
    --page-bg: #f5f5f5;
    --side-bar: #6b6262;
    --red: #e8393c;
    --green: #8bc34a;
    --blue: #1aa3e0;
    --ink: #222;
    --muted: #555;
    --rule: #9a9a9a;
    --list-bg: #ebebeb;
    --list-active: #7a7474;
    --footer-bg: #ebebeb;
  }
  * { box-sizing: border-box; margin: 0; padding: 0; }
  html, body { width: 1200px; height: 1200px; overflow: hidden; }
  body {
    position: relative;
    background: var(--page-bg);
    font-family: "Roboto Condensed", sans-serif;
    color: var(--ink);
  }
  .abs { position: absolute; }

  .side-bar { left: 1110px; top: 0; width: 90px; height: 898px; background: var(--side-bar); }
  .side-bar svg { position: absolute; left: 28px; top: 418px; }

  .brand { left: 124px; top: 60px; display: flex; align-items: center; gap: 12px; }
  .brand-dot { width: 34px; height: 34px; border-radius: 50%; background: var(--blue); }
  .brand-name { font-family: "Open Sans", sans-serif; font-size: 50px; font-weight: 400; color: var(--ink); }

  .nav-btn {
    top: 67px; height: 47px; color: #fff; font-size: 22px;
    display: flex; align-items: center; justify-content: center;
  }
  .nav-login { left: 732px; width: 80px; background: var(--red); }
  .nav-register { left: 822px; width: 104px; background: var(--red); }
  .nav-posts { left: 938px; width: 112px; background: var(--green); }

  .field {
    top: 188px; height: 48px; border: 2px solid var(--rule); background: #f0f0f0;
    color: #b5b5b5; font-size: 23px; padding-left: 16px; display: flex; align-items: center;
  }
  .field-skills { left: 90px; width: 548px; }
  .field-location { left: 689px; width: 261px; }
  .search-btn { left: 1000px; top: 188px; width: 50px; height: 48px; background: #666; display: flex; align-items: center; justify-content: center; }

  .tab { left: 90px; width: 244px; text-align: center; }
  .tab-cv { top: 280px; font-size: 22px; height: 33px; border-bottom: 3px solid var(--red); }
  .tab-job { top: 342px; font-size: 27px; height: 35px; border-bottom: 3px solid var(--green); }

  .skills { left: 90px; top: 404px; width: 244px; }
  .skills h2 {
    font-weight: 400; font-size: 29px; color: var(--blue); text-align: center;
    height: 38px; border-bottom: 3px solid var(--side-bar);
  }
  .skills ul { list-style: none; }
  .skills li {
    height: 36.8px; background: var(--list-bg); border-bottom: 1px solid var(--rule);
    display: flex; align-items: center; justify-content: center;
    font-family: "Open Sans", sans-serif; font-size: 19px; color: var(--blue); position: relative;
  }
  .skills li:last-child { border-bottom: none; }
  .skills li.is-active { background: var(--list-active); }
  .skills li.is-active svg { position: absolute; right: 10px; top: 10px; }

  .section-title { font-weight: 400; color: var(--muted); }
  .howto-title { left: 668px; top: 338px; font-size: 29px; }
  .news-title { left: 638px; top: 643px; font-size: 30px; }

  .howto { top: 397px; width: 171px; border-top: 1px solid var(--rule); }
  .howto p {
    font-family: "Montserrat", sans-serif; font-size: 13.4px; line-height: 18px; color: var(--muted);
    text-align: justify; padding: 16px 4px 0; height: 149px; border-bottom: 1px solid var(--rule);
  }
  .howto p b { color: var(--red); letter-spacing: 2px; }
  .howto h3 {
    font-family: "Montserrat", sans-serif; font-weight: 500; font-size: 16.5px; line-height: 23px;
    text-align: center; color: var(--muted); padding-top: 6px;
  }
  .howto h3.is-featured { color: var(--red); }
  .col-1 { left: 393px; } .col-2 { left: 636px; } .col-3 { left: 879px; }

  .article { top: 702px; width: 171px; height: 151px; }
  .article-head {
    height: 23px; background: var(--red); color: #fff; font-weight: 700; font-style: italic;
    font-size: 20px; text-align: center; line-height: 23px;
  }
  .article-media { height: 104px; padding: 18px 4px 0; color: #fff; font-family: "Open Sans", sans-serif; font-weight: 600; font-size: 11px; line-height: 18px; text-align: justify; }
  .media-blue { background: linear-gradient(160deg, #3f7fb0, #1e4f7e); }
  .media-dark { background: linear-gradient(160deg, #6a6a6a, #262626); }
  .media-tech { background: linear-gradient(160deg, #2f6fb8, #4aa0d8); }
  .article-foot { height: 24px; background: var(--green); color: #fff; font-size: 21px; text-align: center; line-height: 24px; }

  .site-footer { left: 0; top: 898px; width: 1200px; height: 302px; background: var(--footer-bg); }
  .footer-col { top: 78px; list-style: none; font-size: 13px; color: #444; }
  .footer-col li { height: 28px; }
  .footer-col li.is-hover { color: var(--blue); }
  .fc-1 { left: 91px; } .fc-2 { left: 387px; } .fc-3 { left: 684px; } .fc-4 { left: 980px; }
  .copyright { left: 0; top: 279px; width: 1200px; text-align: center; font-family: "Montserrat", sans-serif; font-size: 13px; color: #555; }
</style>
</head>
<body>
  <aside class="abs side-bar">
    <svg width="28" height="64" viewBox="0 0 28 64" fill="none" stroke="#fff" stroke-width="2.5">
      <path d="M14 2 L4 32 L14 62"/><path d="M24 2 L14 32 L24 62"/>
    </svg>
  </aside>

  <header>
    <div class="abs brand"><span class="brand-dot"></span><span class="brand-name">Brightvale</span></div>
    <a class="abs nav-btn nav-login">Login</a>
    <a class="abs nav-btn nav-register">Register</a>
    <a class="abs nav-btn nav-posts">My posts</a>

    <div class="abs field field-skills">search for candidates by skills or ...</div>
    <div class="abs field field-location">Location...</div>
    <div class="abs search-btn">
      <svg width="30" height="30" viewBox="0 0 30 30" fill="none" stroke="#fff" stroke-width="3">
        <circle cx="12" cy="12" r="9"/><path d="M19 19 L28 28"/>
      </svg>
    </div>
  </header>

  <div class="abs tab tab-cv">50 New CV-s added today</div>
  <div class="abs tab tab-job">Post a job</div>

  <nav class="abs skills">
    <h2>Emploies by Skills</h2>
    <ul>
      <li>Emploies by Skills</li>
      <li>Emploies by Skills</li>
      <li class="is-active">Emploies by Skills
        <svg width="18" height="18" viewBox="0 0 18 18" fill="none" stroke="#fff" stroke-width="1.4"><path d="M2 2 L16 8 L9 10 L7 16 Z"/></svg>
      </li>
      <li>Emploies by Skills</li>
      <li>Emploies by Skills</li>
      <li>Emploies by Skills</li>
      <li>Emploies by Skills</li>
      <li>Emploies by Skills</li>
      <li>Emploies by Skills</li>
      <li>Emploies by Skills</li>
      <li>Emploies by Skills</li>
    </ul>
  </nav>

  <h2 class="abs section-title howto-title">How to...</h2>

  <section class="abs howto col-1">
    <p>Lorem ipsum dolor sit amet, consecteturdoe adipisicing elit, sed do eiusmod tempor inci-didunt labore dolore magna aliqua. <b>...</b></p>
    <h3 class="is-featured">How to find the perfect employee?</h3>
  </section>
  <section class="abs howto col-2">
    <p>Lorem ipsum dolor sit amet, consecteturdoe adipisicing elit, sed do eiusmod tempor inci-didunt labore dolore magna aliqua. <b>...</b></p>
    <h3>How to act durring the interview?</h3>
  </section>
  <section class="abs howto col-3">
    <p>Lorem ipsum dolor sit amet, consecteturdoe adipisicing elit, sed do eiusmod tempor inci-didunt labore dolore magna aliqua. <b>...</b></p>
    <h3>How to go to an interview?</h3>
  </section>

  <h2 class="abs section-title news-title">News and articles</h2>

  <article class="abs article col-1">
    <div class="article-head">Lorem ipsum dolor</div>
    <div class="article-media media-blue" role="img" aria-label="Photo of digital data graphics">Lorem ipsum dolor sit amet, consectetur adipisic-ing elit, sed do eiusmod tempor ...</div>
    <div class="article-foot">Reed full article</div>
  </article>
  <article class="abs article col-2">
    <div class="article-head">Lorem ipsum dolor</div>
    <div class="article-media media-dark" role="img" aria-label="Photo of a globe with world map">Lorem ipsum dolor sit amet, consectetur adipisic-ing elit, sed do eiusmod tempor ...</div>
    <div class="article-foot">Reed full article</div>
  </article>
  <article class="abs article col-3">
    <div class="article-head">Lorem ipsum dolor</div>
    <div class="article-media media-tech" role="img" aria-label="Photo of web technology concept">Lorem ipsum dolor sit amet, consectetur adipisic-ing elit, sed do eiusmod tempor ...</div>
    <div class="article-foot">Reed full article</div>
  </article>

  <footer class="abs site-footer">
    <ul class="abs footer-col fc-1">
      <li>Lorem ipsum</li><li>Sit amet</li><li>Labore et dolore</li><li>Magna aliqua</li><li>Ut enim ad minim</li><li>Veniam quis</li>
    </ul>
    <ul class="abs footer-col fc-2">
      <li>Lorem ipsum re et dolore</li><li>Sit ametre et dolore</li><li>Labore et dolore</li><li>Magna aliquaim ad minim</li><li>Ut enim ad minim</li><li>Veniam quis&nbsp; aliquaim</li>
    </ul>
    <ul class="abs footer-col fc-3">
      <li>Lorem ipsum</li><li>Sit amet</li><li>Labore et dolore</li><li class="is-hover">Magna aliqua</li><li>Ut enim ad minim</li><li>Veniam quis</li>
    </ul>
    <ul class="abs footer-col fc-4">
      <li>Lorem ipsum re et dolore</li><li>Sit ametre et dolore</li><li>Labore et dolore</li><li>Magna aliquaim ad minim</li><li>Ut enim ad minim</li><li>Veniam quis&nbsp; aliquaim</li>
    </ul>
    <p class="abs copyright">Copyright © Brightvale 2015</p>
  </footer>
</body>
</html>
```